My project benefits Military, First Responders, Police, Fire, and Educators.

Contact Information for Business Card

2 Sided appointment card. Visual side will have my head shot with "Kestrel Works" in a bold graffic/text. I am picturing maybe the headshot applied to a filter that has a matrix effect where the picture is made up of data/numbers flowing vertically through the photo. I am of course open to other concepts as well. Side two will have contact info presented in an attractive visual complimenting the front.

```html
<!DOCTYPE html>
<html lang="en">
<head>
<meta charset="utf-8">
<title>Kestrel Works – Appointment Card</title>
<link rel="stylesheet" href="https://fonts.googleapis.com/css2?family=Cinzel:wght@700&family=Libre+Baskerville&display=swap">
<style>
  :root {
    --page-bg: #3a3a3c;
    --card-black: #050805;
    --matrix-deep: #06200e;
    --matrix-mid: #0f4a22;
    --matrix-glow: #2f9a4c;
    --panel: #ececec;
    --ink: #1b1b1b;
    --rule: #2a2a2a;
    --watermark: #d9d9d9;
    --title: #f4f1e6;
    --title-gold: #e8c87a;
  }
  * { box-sizing: border-box; margin: 0; padding: 0; }
  html, body { width: 1200px; height: 900px; overflow: hidden; }
  body {
    background: var(--page-bg);
    position: relative;
    font-family: "Libre Baskerville", "Times New Roman", serif;
  }
  .card {
    position: absolute;
    left: 250px;
    width: 700px;
    height: 400px;
    border-radius: 2px;
    overflow: hidden;
    box-shadow: 0 12px 30px rgba(0,0,0,.45);
  }

  /* ---------- Back: appointment side ---------- */
  .card--back {
    top: 40px;
    background:
      radial-gradient(ellipse at 85% 30%, rgba(47,154,76,.45), transparent 55%),
      radial-gradient(ellipse at 10% 90%, rgba(47,154,76,.3), transparent 50%),
      var(--card-black);
  }
  .card--back .frame-texture {
    position: absolute; inset: 0;
    background: linear-gradient(90deg, var(--matrix-deep), var(--card-black) 40%, var(--matrix-mid));
    opacity: .6;
  }
  .appointment-panel {
    position: absolute;
    left: 62px; top: 28px; right: 42px; bottom: 48px;
    background: var(--panel);
    color: var(--ink);
  }
  .panel-watermark {
    position: absolute;
    left: 0; right: 0; top: 250px;
    text-align: center;
    font-family: "Cinzel", Georgia, serif;
    font-weight: 700;
    font-size: 40px;
    line-height: 1;
    letter-spacing: 4px;
    color: var(--watermark);
    white-space: nowrap;
  }
  .panel-heading {
    position: absolute;
    right: 24px; top: 110px;
    font-size: 13px;
    line-height: 1;
  }
  .field-row {
    position: absolute;
    left: 20px; right: 24px;
    display: flex;
    align-items: flex-end;
    font-size: 12px;
  }
  .field-row .label { margin-right: 8px; line-height: 1; }
  .field-row .line { flex: 1; border-bottom: 1px solid var(--rule); }
  .field-row--name { top: 30px; left: 56px; }
  .field-row--time { top: 56px; left: 40px; }
  .field-row--desc { top: 82px; left: 20px; }
  .blank-line {
    position: absolute;
    left: 20px; right: 24px;
    border-bottom: 1px solid var(--rule);
  }

  /* ---------- Front: visual side ---------- */
  .card--front {
    top: 470px;
    background:
      radial-gradient(ellipse at 70% 55%, rgba(47,154,76,.55), transparent 60%),
      linear-gradient(160deg, var(--matrix-mid), var(--matrix-deep) 45%, var(--card-black));
  }
  .headshot {
    position: absolute;
    left: 60px; top: 30px;
    width: 270px; height: 370px;
    background:
      radial-gradient(ellipse 38% 30% at 60% 36%, rgba(183,122,58,.9), rgba(183,122,58,0) 100%),
      radial-gradient(ellipse 45% 30% at 35% 92%, rgba(111,143,166,.8), rgba(111,143,166,0) 100%);
  }
  .brand-title {
    position: absolute;
    left: 320px; right: 30px; top: 175px;
    font-family: "Cinzel", Georgia, serif;
    font-weight: 700;
    line-height: 1;
    text-align: center;
    white-space: nowrap;
  }
  .brand-title .line-1 { display: block; font-size: 58px; letter-spacing: 3px; color: var(--title); }
  .brand-title .line-2 { display: block; font-size: 36px; letter-spacing: 3px; margin-top: 8px; color: var(--title-gold); }
</style>
</head>
<body>

  <section class="card card--back" aria-label="Appointment card, back">
    <div class="frame-texture" role="img" aria-label="Green falling-code background"></div>
    <div class="appointment-panel">
      <div class="panel-watermark" aria-hidden="true">KESTREL WORKS</div>
      <div class="field-row field-row--name"><span class="label">Name</span><span class="line"></span></div>
      <div class="field-row field-row--time"><span class="label">Time</span><span class="line"></span></div>
      <div class="field-row field-row--desc"><span class="label">Description</span><span class="line"></span></div>
      <div class="panel-heading">Appointment</div>
      <div class="blank-line" style="top:140px"></div>
      <div class="blank-line" style="top:172px"></div>
      <div class="blank-line" style="top:204px"></div>
      <div class="blank-line" style="top:236px"></div>
    </div>
  </section>

  <section class="card card--front" aria-label="Appointment card, front">
    <div class="headshot" role="img" aria-label="Head-and-shoulders portrait rendered in green falling code"></div>
    <h1 class="brand-title">
      <span class="line-1">KESTREL</span>
      <span class="line-2">WORKS</span>
    </h1>
  </section>

</body>
</html>
```